SANDWICH SKILLET DESIGN (Packaging)

We require a skillet (sandwich box) designed I have uploaded a similar one we have already
I have uploaded the logo to be placed on the skillet
( BRAMBLE GATE PANTRY OWLS LTD)
we would like a sandwich skillet which has a white background and maybe some veg items which maybe found in a sandwich
hope this helps

```html
<!DOCTYPE html>
<html lang="en">
<head>
<meta charset="utf-8">
<title>Sandwich Skillet – Bramble Gate Pantry Owls Ltd</title>
<link rel="stylesheet" href="https://fonts.googleapis.com/css2?family=Oswald:wght@400;600&display=swap">
<style>
  :root {
    --canvas: #c9c7c7;
    --maroon: #8b1a2d;
    --panel-white: #f5f5f5;
    --panel-grey: #ececec;
    --window: #ddd5bb;
    --window-edge: #b9b3a3;
    --photo-red: #c9382c;
    --photo-green: #7fa35a;
    --photo-purple: #8d4f8e;
    --photo-bread: #d9a35c;
    --ink-dark: #2b2b2b;
  }
  * { box-sizing: border-box; margin: 0; padding: 0; }
  html, body { width: 770px; height: 1200px; overflow: hidden; }
  body {
    background: var(--canvas);
    font-family: "Oswald", "Arial Narrow", sans-serif;
    position: relative;
  }
  .skillet-net { position: absolute; inset: 0; }
  .panel { position: absolute; }

  /* side triangle */
  .side-panel { left: 20px; top: 467px; width: 320px; height: 320px; }
  .side-panel svg { display: block; width: 100%; height: 100%; }

  /* front window panel */
  .front-panel {
    left: 378px; top: 413px; width: 165px; height: 374px;
    background: linear-gradient(160deg, #ffffff, var(--panel-white) 60%, #e9e9e9);
    overflow: hidden;
  }
  .front-panel svg { position: absolute; inset: 0; width: 100%; height: 100%; }
  .front-copy {
    position: absolute; left: 0; right: 0; bottom: 6px;
    text-align: center; color: var(--ink-dark);
  }
  .front-copy .product-title {
    font-weight: 600; font-size: 10.5px; letter-spacing: 0.1px; line-height: 1.1;
  }
  .front-copy .storage-note {
    font-size: 5.6px; color: var(--maroon); line-height: 1.2; letter-spacing: 0.2px;
  }

  /* back info panel */
  .back-panel {
    left: 581px; top: 413px; width: 165px; height: 374px;
    background: var(--panel-grey);
    color: var(--maroon);
    text-align: center;
  }
  .allergen-list {
    position: absolute; top: 100px; left: 0; right: 0;
    font-size: 8.4px; line-height: 1.35; letter-spacing: 0.2px;
  }
  .brand-stamp {
    position: absolute; left: 50%; top: 195px; transform: translateX(-50%);
    width: 44px; height: 44px; border-radius: 50%;
    background: #ffffff;
    display: flex; align-items: center; justify-content: center;
    font-size: 4.6px; line-height: 1.2; color: var(--maroon); padding: 4px;
  }
  .company-address {
    position: absolute; top: 252px; left: 0; right: 0;
    font-size: 6.4px; line-height: 1.4; letter-spacing: 0.2px;
  }
</style>
</head>
<body>
<main class="skillet-net">

  <section class="panel side-panel" aria-label="Side panel">
    <svg viewBox="0 0 320 320" xmlns="http://www.w3.org/2000/svg">
      <defs>
        <clipPath id="side-shape"><polygon points="0,0 2,320 320,320"/></clipPath>
        <linearGradient id="veg-tones" x1="0" y1="0" x2="1" y2="1">
          <stop offset="0" stop-color="var(--photo-red)"/>
          <stop offset="0.3" stop-color="var(--photo-bread)"/>
          <stop offset="0.55" stop-color="var(--photo-purple)"/>
          <stop offset="0.8" stop-color="var(--photo-green)"/>
          <stop offset="1" stop-color="#5e7f43"/>
        </linearGradient>
      </defs>
      <g clip-path="url(#side-shape)">
        <rect width="320" height="320" fill="var(--panel-white)"/>
        <rect x="0" y="125" width="320" height="195" fill="url(#veg-tones)"
              role="img" aria-label="Photo of fresh salad vegetables: tomatoes, cucumber, red cabbage and bread"/>
      </g>
      <circle cx="46" cy="282" r="27" fill="#ffffff"/>
      <text x="46" y="280" text-anchor="middle" font-family="Oswald, sans-serif" font-size="5.2" fill="var(--maroon)">BRAMBLE GATE</text>
      <text x="46" y="287" text-anchor="middle" font-family="Oswald, sans-serif" font-size="5.2" fill="var(--maroon)">PANTRY OWLS LTD</text>
    </svg>
  </section>

  <section class="panel front-panel" aria-label="Front window panel">
    <svg viewBox="0 0 165 374" xmlns="http://www.w3.org/2000/svg" preserveAspectRatio="none">
      <path class="top-band" d="M0,0 H165 V30 Q78,24 0,52 Z" fill="var(--maroon)"/>
      <path class="top-stripe" d="M0,66 Q78,38 165,44" fill="none" stroke="var(--maroon)" stroke-width="5"/>
      <path class="window"
            d="M28,52 H138 Q150,52 150,64 V278 Q150,286 142,286 H124 Q112,286 112,298 V326 Q112,336 102,336 H26 Q16,336 16,326 V64 Q16,52 28,52 Z"
            fill="var(--window)" stroke="var(--window-edge)" stroke-width="1"/>
      <rect x="0" y="318" width="22" height="30" fill="var(--photo-red)"
            role="img" aria-label="Edge of vegetable photo showing a tomato"/>
      <circle cx="134" cy="316" r="19" fill="#ffffff" stroke="#e2e2e2" stroke-width="0.8"/>
      <text x="134" y="315" text-anchor="middle" font-family="Oswald, sans-serif" font-size="4" fill="var(--maroon)">BRAMBLE GATE</text>
      <text x="134" y="320" text-anchor="middle" font-family="Oswald, sans-serif" font-size="4" fill="var(--maroon)">PANTRY OWLS LTD</text>
    </svg>
    <div class="front-copy">
      <p class="product-title">FRESHLY HANDMADE SANDWICHES</p>
      <p class="storage-note">EAT ON DAY OF PURCHASE KEEP REFRIGERATED</p>
      <p class="storage-note">BELOW 5° degrees</p>
    </div>
  </section>

  <section class="panel back-panel" aria-label="Back information panel">
    <p class="allergen-list">
      MAY CONTAIN LUPIN, MOLLUSCS<br>
      MILK,BARLEY, SESAME SEEDS<br>
      CRUSTACEANS,FISH,SULPHITES,SOYA<br>
      CELERY &amp; NUTS
    </p>
    <div class="brand-stamp">BRAMBLE GATE PANTRY OWLS LTD</div>
    <p class="company-address">
      BRAMBLE GATE PANTRY OWLS LTD<br>
      UNIT 4 ORCHARD ROW<br>
      BG12 7PQ
    </p>
  </section>

</main>
</body>
</html>
```